Playful, Modern Brochure Design for informing about managed services provided

For our Managed Services we are looking for a brochure with simple explanation of the services we offer. Brochure not a full text brochure. Something like a summation with prices of the options we provide. Think about monitoring, VOIP, anti-virus, tessera 480 etc.

combination of Who We Are and products offering in a simple overview.

a bit similar to https://leaflet.pimovarta.com/contest.aspx?id=3847102

it’s about professional services, security and stability of the customers IT, so the design should express that.

Target Market(s)

Business to Business

Font styles to use
Sans Serif
Other font styles liked:
• Arial

Colors

Designer to choose colors to be used in the design.

Requirements
Must have
• attractive front which invites to read further, inside summation of services.
• Contact Info
• Icons for services:
• Hosting, Security, Monitoring, Cloud, VOIP, Online Backup
Nice to have
• Other icons like Tessera 480, firewall, proxy server and other thinkable.
Should not have
• Pages with large amount of text.

```html
<!DOCTYPE html>
<html lang="nl">
<head>
<meta charset="utf-8">
<title>Managed Services Brochure – Inside Spread</title>
<link href="https://fonts.googleapis.com/css2?family=Roboto+Condensed:wght@400;700&family=Open+Sans:wght@400;600&display=swap" rel="stylesheet">
<style>
  :root {
    --bg: #e9ebee;
    --paper: #f4f6fa;
    --blue: #3b86d4;
    --blue-light: #62a6e2;
    --red: #c9343c;
    --pink: #c2255c;
    --sky: #4aa2d8;
    --grey: #6f6f71;
    --grey-dark: #555659;
    --text: #6a6d73;
    --white: #ffffff;
  }
  * { box-sizing: border-box; margin: 0; padding: 0; }
  html, body { width: 1200px; height: 789px; overflow: hidden; background: var(--bg); }
  body { font-family: "Open Sans", Arial, sans-serif; color: var(--text); position: relative; }

  .spread { position: absolute; left: 40px; top: 20px; width: 1120px; height: 749px; display: flex; box-shadow: 0 8px 24px rgba(0,0,0,.18); }
  .page { position: relative; width: 560px; height: 749px; background: var(--paper); overflow: hidden; }
  .page--left { border-right: 1px solid #dfe2e7; }

  .photo { position: absolute; }
  .photo--office { left: 0; top: 0; width: 560px; height: 175px; background: linear-gradient(120deg, #d9dde3 0%, #f1f2f4 45%, #b9bfc7 70%, #8a3b36 100%); }
  .photo--servers { left: 0; top: 0; width: 560px; height: 255px; background: linear-gradient(100deg, #0d1f6b 0%, #2a4fd0 40%, #9fb6f0 62%, #2947c4 82%, #0b1b5e 100%); }
  .photo--phone { left: 16px; top: 44px; width: 98px; height: 172px; background: linear-gradient(160deg, #c8b89a 0%, #6b5a44 45%, #1d1f2a 100%); }
  .photo--team { inset: 8px; border-radius: 50%; background: linear-gradient(130deg, #e6e9ee 0%, #b8c3d4 45%, #2c3f6e 75%, #d9dde3 100%); }

  .tab-desktop { position: absolute; left: 392px; top: 78px; width: 168px; height: 200px; background: var(--grey); padding: 28px 0 0 16px; }
  .tab-desktop h2 { font-family: "Roboto Condensed", Arial, sans-serif; font-weight: 700; color: var(--white); font-size: 33px; line-height: 1.05; letter-spacing: 1px; }

  .headline { position: absolute; font-family: "Roboto Condensed", Arial, sans-serif; font-weight: 700; font-size: 40px; letter-spacing: 1px; color: var(--blue); }
  .headline--light { color: var(--white); }

  .lead { position: absolute; font-size: 10.5px; line-height: 1.45; }
  .service { position: absolute; width: 170px; }
  .service h3 { font-family: "Roboto Condensed", Arial, sans-serif; font-weight: 400; font-size: 13px; letter-spacing: .3px; margin-bottom: 3px; }
  .service p { font-size: 8.5px; line-height: 1.4; }
  .service--red h3 { color: var(--red); }
  .service--pink h3 { color: var(--pink); }
  .service--sky h3 { color: var(--sky); }

  .about { position: absolute; left: 40px; top: 475px; width: 310px; font-size: 10.5px; line-height: 1.4; text-align: justify; }
  .about p + p { margin-top: 10px; }

  .halo { position: absolute; border-radius: 50%; background: rgba(214,226,242,.55); }

  .phone { position: absolute; left: 356px; top: 415px; width: 130px; height: 262px; border: 2px solid #c9ccd2; border-radius: 22px; background: var(--white); }
  .phone__speaker { position: absolute; left: 50px; top: 20px; width: 28px; height: 4px; border-radius: 2px; background: #c9ccd2; }
  .phone__button { position: absolute; left: 52px; top: 226px; width: 24px; height: 24px; border-radius: 50%; border: 2px solid #c9ccd2; }

  .team { position: absolute; left: 376px; top: 470px; width: 168px; height: 168px; border-radius: 50%; border: 4px solid var(--grey); background: var(--white); }

  .wave { position: absolute; left: 0; bottom: 0; width: 560px; }
  .footer-line { position: absolute; display: flex; align-items: center; gap: 8px; color: var(--white); font-size: 15px; letter-spacing: .5px; }
  .footer-line svg { width: 15px; height: 15px; }
  .newsletter { position: absolute; right: 30px; bottom: 58px; color: var(--white); font-family: "Roboto Condensed", Arial, sans-serif; font-size: 21px; }
</style>
</head>
<body>
<main class="spread">

  <section class="page page--left">
    <div class="photo photo--office" role="img" aria-label="Man in a checked shirt working at a desktop computer in a bright open office"></div>
    <div class="tab-desktop"><h2>DESKTOP<br>PACKAGE</h2></div>

    <p class="lead" style="left:30px; top:188px; width:350px;">Lorem ipsum dolor sit amet, consectetur adipiscing elit, sed do eiusmod temporincididunt ut labore et dolore magna aliqua.Lorem ipsum dolor sit amet, consectetur adipiscing elit, sed do eiusmod temporincididunt ut labore et dolore magna aliqua.</p>

    <div class="service service--red" style="left:30px; top:252px;"><h3>MONITORING</h3><p>Lorem ipsum dolor sit amet, consectetur adipiscing elit, sed do eiusmod</p></div>
    <div class="service service--pink" style="left:205px; top:282px;"><h3>PATCH MANAGEMENT</h3><p>Lorem ipsum dolor sit amet, consectetur adipiscing elit, sed do eiusmod</p></div>
    <div class="service service--sky" style="left:385px; top:318px;"><h3>ANTI-VIRUS</h3><p>Lorem ipsum dolor sit amet, consectetur adipiscing elit, sed do eiusmod</p></div>

    <div class="halo" style="left:300px; top:360px; width:220px; height:220px;"></div>

    <h2 class="headline" style="left:30px; top:330px;">MOBILE PACKAGE</h2>
    <p class="lead" style="left:30px; top:382px; width:290px;">Lorem ipsum dolor sit amet, consectetur adipiscing elit, sed do eiusmod temporincididunt ut labore et dolore magna aliqua.Lorem ipsum dolor</p>

    <div class="service service--red" style="left:30px; top:440px;"><h3>MONITORING</h3><p>Lorem ipsum dolor sit amet, consectetur adipiscing elit, sed do eiusmod</p></div>
    <div class="service service--pink" style="left:185px; top:470px;"><h3>PATCH MANAGEMENT</h3><p>Lorem ipsum dolor sit amet, consectetur adipiscing elit, sed do eiusmod</p></div>
    <div class="service service--sky" style="left:30px; top:498px; width:260px;"><h3>ANTI-VIRUS</h3><p>Lorem ipsum dolor sit amet, consectetur adipiscing elit, sed do eiusmod</p></div>

    <svg class="wave" height="230" viewBox="0 0 560 230" aria-hidden="true">
      <path d="M0 50 C 180 110, 380 150, 560 140 L560 230 L0 230 Z" fill="var(--grey-dark)"/>
      <path d="M0 62 C 180 122, 380 162, 560 152 L560 230 L0 230 Z" fill="var(--paper)"/>
      <path d="M0 70 C 180 130, 380 170, 560 160 L560 230 L0 230 Z" fill="var(--blue)"/>
      <path d="M0 140 C 200 190, 400 210, 560 200 L560 230 L0 230 Z" fill="var(--blue-light)" opacity=".5"/>
    </svg>

    <div class="phone">
      <span class="phone__speaker"></span>
      <div class="photo photo--phone" role="img" aria-label="Young woman outdoors looking at her smartphone"></div>
      <span class="phone__button"></span>
    </div>

    <div class="footer-line" style="left:30px; top:662px;">
      <svg viewBox="0 0 16 16" fill="none" stroke="currentColor" stroke-width="1.4"><circle cx="8" cy="8" r="6.5"/><path d="M1.5 8h13M8 1.5c2.2 2 2.2 11 0 13M8 1.5c-2.2 2-2.2 11 0 13"/></svg>
      <span>www.velora.nl</span>
    </div>
  </section>

  <section class="page page--right">
    <div class="photo photo--servers" role="img" aria-label="Data centre corridor lined with illuminated server racks"></div>
    <h2 class="headline headline--light" style="left:14px; top:200px;">SERVER PACKAGE</h2>

    <p class="lead" style="left:20px; top:262px; width:470px;">Lorem ipsum dolor sit amet, consectetur adipiscing elit, sed do eiusmod temporincididunt ut labore et dolore magna aliqua.</p>

    <div class="service service--red" style="left:20px; top:316px;"><h3>MONITORING</h3><p>Lorem ipsum dolor sit amet, consectetur adipiscing elit, sed do eiusmod</p></div>
    <div class="service service--pink" style="left:190px; top:346px;"><h3>PATCH MANAGEMENT</h3><p>Lorem ipsum dolor sit amet, consectetur adipiscing elit, sed do eiusmod</p></div>
    <div class="service service--sky" style="left:380px; top:378px;"><h3>ANTI-VIRUS</h3><p>Lorem ipsum dolor sit amet, consectetur adipiscing elit, sed do eiusmod</p></div>

    <h2 class="headline" style="left:40px; top:422px;">WHO WE ARE</h2>
    <div class="about">
      <p>Onze klanten schijnen nogal gecharmeerd te zijn van onze proactieve mentaliteit. We houden er namelijk van om adequaat te adviseren en snel resultaat te laten zien. Daarbij stemmen wij onze dienstverlening geheel af op uw wensen; om voor elk project het maximale resultaat te behalen, werken we met maatwerkoplossingen.</p>
      <p>Lorem ipsum dolor sit amet, consectetur adipiscing elit, sed do eiusmod temporincididunt ut labore et dolore magna aliqua.Lorem ipsum dolor sit amet.</p>
    </div>

    <svg class="wave" height="130" viewBox="0 0 560 130" aria-hidden="true">
      <path d="M0 22 C 160 40, 360 30, 560 0 L560 130 L0 130 Z" fill="var(--grey-dark)"/>
      <path d="M0 34 C 160 52, 360 42, 560 12 L560 130 L0 130 Z" fill="var(--paper)"/>
      <path d="M0 42 C 160 60, 360 50, 560 20 L560 130 L0 130 Z" fill="var(--blue)"/>
      <path d="M200 130 C 320 95, 450 80, 560 65 L560 130 Z" fill="var(--blue-light)" opacity=".5"/>
    </svg>

    <div class="team">
      <div class="photo photo--team" role="img" aria-label="Smiling businesswoman in front of colleagues in a meeting room"></div>
    </div>

    <p class="newsletter">Meld je aan voor onze nieuwsbrief</p>
    <div class="footer-line" style="right:30px; bottom:26px;">
      <svg viewBox="0 0 16 16" fill="none" stroke="currentColor" stroke-width="1.4"><circle cx="8" cy="8" r="6.5"/><rect x="4.5" y="5.5" width="7" height="5" rx=".5"/><path d="M4.5 5.8 8 8.5l3.5-2.7"/></svg>
      <span>info@velora.nl</span>
    </div>
  </section>

</main>
</body>
</html>
```